RTamberly Business Cards & Letterhead

I have a logo but need a design for some new business cards. We are a Design-Build Firm that specializes in the design and construction of commercial projects.
the cards need to be professional. no cartoon stuff.
i would like to have the cards in AI format so I can update the card as needed. Logo is provided.
Our Address is: 4183 Marwood Ln. Apex, North Carolina 27614

```html
<!DOCTYPE html>
<html lang="en">
<head>
<meta charset="utf-8">
<title>RTamberly Business Card</title>
<link href="https://fonts.googleapis.com/css2?family=Open+Sans:wght@400;600;700;800&display=swap" rel="stylesheet">
<style>
  :root {
    --bg: #333333;
    --card-dark: #212125;
    --blue-deep: #0b3a63;
    --blue-mid: #0f5d97;
    --blue-bright: #1a7fc4;
    --band: #0f4f84;
    --text-light: #ffffff;
    --text-grey: #56585e;
  }
  * { box-sizing: border-box; margin: 0; padding: 0; }
  html, body { width: 1200px; height: 780px; overflow: hidden; }
  body {
    background: var(--bg);
    font-family: "Open Sans", Arial, sans-serif;
    display: flex;
    align-items: center;
    justify-content: center;
    gap: 40px;
  }
  .card {
    position: relative;
    width: 540px;
    height: 309px;
    border-radius: 18px;
    overflow: hidden;
  }

  /* Back side */
  .card-back {
    background: linear-gradient(160deg, var(--blue-mid) 0%, var(--blue-deep) 60%, #072b4a 100%);
  }
  .back-pattern {
    position: absolute;
    inset: 0;
    background: linear-gradient(200deg, rgba(40,130,200,0.35) 0%, rgba(8,40,70,0.25) 100%);
  }
  .back-wordmark {
    position: absolute;
    left: 50%;
    top: 50%;
    transform: translate(-50%, -50%);
    display: flex;
    align-items: center;
    gap: 12px;
    color: var(--text-light);
    font-weight: 800;
    font-size: 44px;
    letter-spacing: 1px;
  }
  .back-wordmark .mark-square {
    width: 30px; height: 30px; background: var(--text-light);
  }

  /* Front side */
  .card-front { background: var(--card-dark); }
  .front-emblem {
    position: absolute;
    left: 0; top: 40px;
    width: 210px; height: 235px;
    border-radius: 0 26px 26px 0;
    background: linear-gradient(150deg, var(--blue-bright) 0%, var(--blue-mid) 50%, var(--blue-deep) 100%);
  }
  .front-wordmark {
    position: absolute;
    right: 42px; top: 28px;
    display: flex; align-items: center; gap: 10px;
    color: var(--text-grey);
    font-weight: 800;
    font-size: 38px;
    letter-spacing: 1px;
  }
  .front-wordmark .mark-square {
    width: 24px; height: 24px; background: var(--blue-mid);
  }
  .name-band {
    position: absolute;
    left: 230px; right: 0; top: 92px;
    height: 56px;
    background: linear-gradient(90deg, rgba(15,79,132,0) 0%, var(--band) 30%, var(--band) 100%);
    text-align: right;
    padding: 6px 24px 0 0;
    color: var(--text-light);
  }
  .name-band .person-name {
    font-weight: 800; font-size: 24px; letter-spacing: 1px; line-height: 1.1;
  }
  .name-band .person-title {
    font-weight: 600; font-size: 14px; letter-spacing: 0.5px;
  }
  .contact {
    position: absolute;
    right: 24px; top: 162px;
    text-align: right;
    color: var(--text-light);
    font-size: 14px;
    line-height: 1.35;
  }
  .contact .address { margin-bottom: 10px; padding-right: 26px; }
  .contact-line { display: flex; justify-content: flex-end; align-items: center; gap: 8px; }
  .contact-line svg { width: 16px; height: 16px; fill: var(--blue-bright); }
</style>
</head>
<body>

  <section class="card card-back">
    <div class="back-pattern" role="img" aria-label="Repeating brand monogram pattern in shades of blue"></div>
    <div class="back-wordmark"><span class="mark-square"></span>RTAMBERLY</div>
  </section>

  <section class="card card-front">
    <div class="front-emblem" role="img" aria-label="Large blue brand monogram emblem"></div>
    <div class="front-wordmark"><span class="mark-square"></span>RTAMBERLY</div>

    <div class="name-band">
      <div class="person-name">NORMAN TAMBERLY</div>
      <div class="person-title">Founder/President</div>
    </div>

    <div class="contact">
      <div class="address">4183 Marwood Ln. Apex,<br>North Carolina 27614</div>
      <div class="contact-line">(919) 555-0148
        <svg viewBox="0 0 16 16"><path d="M3.5 1.5l2.5 0 1 3.5-1.6 1.2a8 8 0 0 0 4.4 4.4L11 9l3.5 1v2.5c0 1-1 2-2 2A11 11 0 0 1 1.5 3.5c0-1 1-2 2-2z"/></svg>
      </div>
      <div class="contact-line">www.rtamberly.com
        <svg viewBox="0 0 16 16"><circle cx="8" cy="8" r="6.5" fill="none" stroke="#1a7fc4" stroke-width="1.5"/><path d="M1.5 8h13M8 1.5c2.5 2.5 2.5 10.5 0 13M8 1.5c-2.5 2.5-2.5 10.5 0 13" fill="none" stroke="#1a7fc4" stroke-width="1.2"/></svg>
      </div>
      <div class="contact-line">NRT@RTamberly.com
        <svg viewBox="0 0 16 16"><rect x="1.5" y="3.5" width="13" height="9" rx="1" fill="none" stroke="#1a7fc4" stroke-width="1.5"/><path d="M1.5 4l6.5 5 6.5-5" fill="none" stroke="#1a7fc4" stroke-width="1.5"/></svg>
      </div>
    </div>
  </section>

</body>
</html>
```